依頼概要
【依頼の目的・概要】
電子書籍の表紙デザインをお願いします。

【本の内容】
ヒプノセラピー(催眠療法)という手法を使い、
潜在意識にアクセスして、本来の自分と出会い
満たされた人生を送りましょうという主旨の本です。

前半は『虫の知らせ』や『以心伝心』などちょっぴり不思議な話を扱い、
潜在意識とは精神世界とは何か、に触れています。

後半は具体的なヒプノセラピーの手法について解説しています。
暗示療法、年齢退行療法、前世療法を事例を挙げながら説明しています。
最後にペンデュラムの使い方を解説しています。

【書籍タイトル】
胸のざわめきを静めて毎日を整える「内なる声の聴き方」

【著者名】
宮内ちえ美
(本名は”宮内智恵美”ですがちょっと柔らかい印象があると思い、ひらがなを使っています)

◆デザイン要望
デザイナーさんにお任せしたいです。

不明点やご質問がございましたら、お気軽にお尋ね下さい。
宜しくお願い致します。

*業種と区別の中に、私の仕事の該当業種がありませんでしたが、
セラピーのセッション、セラピストの育成です。
*原稿を添付します。
*写真はまだ撮れていないため、添付していません。
2月4日に撮影予定ですが、表紙に使用するかどうかは未定です。
*私自身のページをお見せするものがないのですが、facebookは、Murzalin Chiemi (高田)で出てきます。
LPは作成予定です。

かわいらしく素敵で、とても暖かい気持ちになる表紙でした。 しっとりとした落ち着きのあるところもいいなあと思いました。 イラストを扉に変えて頂き、さらに暖かさが増したように思いました。 扉の方の納品をお願いいたします。イラスト変更ご対応いただき、ありがとうございました。

分かりやすく、シンプルで、内容も書いてあり、電子書籍に映えると思いました。

皆さま、たくさんのご応募をありがとうございました。
どの案も素晴らしく個性的で1つに絞るのが本当に大変でした。

実際に書籍を読んで下さったり、テーマに興味を持って描いてくださったりされた デザイナーさんもいらして、本当に真摯に取り組んで頂き、ありがとうございました。
心よりお礼を申し上げます。

皆様のご活躍をお祈りしております。

```html
<!DOCTYPE html>
<html lang="ja">
<head>
<meta charset="utf-8">
<title>胸のざわめきを静めて毎日を整える「内なる声の聴き方」</title>
<link rel="stylesheet" href="https://fonts.googleapis.com/css2?family=Noto+Sans+JP:wght@700;900&display=swap">
<style>
  :root {
    --bg-deep: #35288a;
    --bg-mid: #5246b8;
    --bg-light: #7a6fe0;
    --title-white: #ffffff;
    --accent-yellow: #f6e72c;
  }
  html, body {
    margin: 0;
    padding: 0;
    width: 752px;
    height: 1200px;
    overflow: hidden;
    background: var(--bg-deep);
  }
  .cover {
    position: relative;
    width: 752px;
    height: 1200px;
    overflow: hidden;
    font-family: "Noto Sans JP", sans-serif;
  }
  .cover__backdrop {
    position: absolute;
    inset: 0;
    display: block;
  }
  .vertical {
    position: absolute;
    writing-mode: vertical-rl;
    text-orientation: upright;
    margin: 0;
    white-space: nowrap;
  }
  .subtitle {
    color: var(--accent-yellow);
    font-weight: 900;
    font-size: 46px;
    line-height: 1;
    letter-spacing: 0;
    text-shadow: 0 2px 6px rgba(20, 10, 70, 0.45);
  }
  .subtitle--first { top: 48px; left: 656px; }
  .subtitle--second { top: 48px; left: 590px; }
  .title {
    color: var(--title-white);
    font-weight: 900;
    font-size: 172px;
    line-height: 1;
    letter-spacing: 4px;
    text-shadow: 0 4px 12px rgba(20, 10, 70, 0.45);
  }
  .title--first { top: 40px; left: 388px; }
  .title--second { top: 40px; left: 96px; }
  .author-credential {
    color: var(--title-white);
    font-weight: 700;
    font-size: 28px;
    line-height: 1;
    top: 780px;
    left: 150px;
    text-shadow: 0 2px 6px rgba(20, 10, 70, 0.5);
  }
  .author-name {
    color: var(--title-white);
    font-weight: 900;
    font-size: 62px;
    line-height: 1;
    top: 780px;
    left: 192px;
    text-shadow: 0 3px 8px rgba(20, 10, 70, 0.5);
  }
</style>
</head>
<body>
  <main class="cover">
    <svg class="cover__backdrop" width="752" height="1200" viewBox="0 0 752 1200" role="img" aria-label="紫色の迷路が遠くまで広がる背景イラスト">
      <defs>
        <radialGradient id="maze-glow" cx="0.5" cy="0.55" r="0.75">
          <stop offset="0" stop-color="var(--bg-light)"/>
          <stop offset="0.55" stop-color="var(--bg-mid)"/>
          <stop offset="1" stop-color="var(--bg-deep)"/>
        </radialGradient>
      </defs>
      <rect width="752" height="1200" fill="url(#maze-glow)"/>
    </svg>

    <p class="vertical subtitle subtitle--first">胸のざわめきを静めて</p>
    <p class="vertical subtitle subtitle--second">毎日を整える</p>

    <h1 class="vertical title title--first">内なる声</h1>
    <h1 class="vertical title title--second">の聴き方</h1>

    <p class="vertical author-credential">認定心理士</p>
    <p class="vertical author-name">宮内ちえ美</p>
  </main>
</body>
</html>
```